Copper Gavel Auctions business card design with existing logo

Looking for a sleek and sexy design using our current logo

Contact Information for Business Card

Name, address, email, phone, website. Marcus Delvane 418 Birchmont Road Suite 200C Fenwick NY 11093 Copperbidhouse.net (631)582-4067

```html
<!DOCTYPE html>
<html lang="en">
<head>
<meta charset="utf-8">
<title>Copper Gavel Auctions – Business Card</title>
<link href="https://fonts.googleapis.com/css2?family=Open+Sans:wght@400;700&display=swap" rel="stylesheet">
<style>
  :root {
    --backdrop: #2b2c2e;
    --card: #f1f1f1;
    --navy: #1d3c8f;
    --red: #d5282c;
  }
  * { margin: 0; padding: 0; box-sizing: border-box; }
  html, body { width: 1200px; height: 1000px; overflow: hidden; }
  body {
    background: var(--backdrop);
    position: relative;
    font-family: "Open Sans", Arial, sans-serif;
    color: var(--navy);
  }
  .card {
    position: absolute;
    left: 372px;
    width: 479px;
    height: 282px;
    background: var(--card);
    border-radius: 16px;
  }
  .card-front { top: 172px; }
  .card-back { top: 550px; }

  .brand {
    position: absolute;
    display: flex;
    flex-direction: column;
    align-items: center;
    transform: translateX(-50%);
    text-align: center;
  }
  .brand-mark {
    border-radius: 50%;
    background: var(--red);
    flex: none;
  }
  .brand-name {
    font-weight: 700;
    color: var(--navy);
    text-transform: uppercase;
    letter-spacing: 1px;
    line-height: 1.15;
  }
  .card-front .brand { left: 240px; top: 84px; gap: 9px; }
  .card-front .brand-mark { width: 48px; height: 48px; }
  .card-front .brand-name { font-size: 20px; }
  .card-back .brand { left: 362px; top: 100px; gap: 7px; }
  .card-back .brand-mark { width: 38px; height: 38px; }
  .card-back .brand-name { font-size: 16px; }

  .holder-name {
    position: absolute;
    left: 46px; top: 80px;
    font-size: 17.5px;
    font-weight: 400;
  }
  .contact-list {
    position: absolute;
    left: 46px; top: 119px;
    list-style: none;
    font-size: 12px;
  }
  .contact-item {
    display: flex;
    align-items: center;
    height: 21.6px;
  }
  .contact-item.continued { padding-left: 24px; }
  .contact-icon {
    width: 14px; height: 14px;
    border-radius: 2px;
    background: var(--red);
    margin-right: 7px;
    flex: none;
    display: flex; align-items: center; justify-content: center;
  }
  .contact-icon svg { width: 10px; height: 10px; }
  .divider {
    position: absolute;
    left: 240px; top: 44px;
    width: 1.5px; height: 196px;
    background: var(--navy);
  }
  .social-row {
    position: absolute;
    left: 382px; top: 246px;
    display: flex; gap: 4px;
  }
  .social-dot {
    width: 14.5px; height: 14.5px;
    border-radius: 50%;
    background: var(--navy);
  }
</style>
</head>
<body>
  <section class="card card-front">
    <div class="brand">
      <span class="brand-mark"></span>
      <span class="brand-name">Copper Gavel<br>Auctions</span>
    </div>
  </section>

  <section class="card card-back">
    <h1 class="holder-name">Marcus Delvane</h1>
    <ul class="contact-list">
      <li class="contact-item">
        <span class="contact-icon"><svg viewBox="0 0 10 10"><path d="M2.2 1 L3.8 1 L4.3 3 L3.3 3.8 Q4.2 5.8 6.2 6.7 L7 5.7 L9 6.2 L9 7.8 Q9 9 7.8 9 Q1 8.5 1 2.2 Q1 1 2.2 1Z" fill="#fff"/></svg></span>
        (631)582-4067
      </li>
      <li class="contact-item">
        <span class="contact-icon"><svg viewBox="0 0 10 10"><rect x="1" y="2.2" width="8" height="5.6" fill="none" stroke="#fff" stroke-width="1"/><path d="M1 2.4 L5 5.4 L9 2.4" fill="none" stroke="#fff" stroke-width="1"/></svg></span>
        info@copperbidhouse.net
      </li>
      <li class="contact-item">
        <span class="contact-icon"><svg viewBox="0 0 10 10"><circle cx="5" cy="5" r="3.8" fill="none" stroke="#fff" stroke-width="0.9"/><ellipse cx="5" cy="5" rx="1.6" ry="3.8" fill="none" stroke="#fff" stroke-width="0.8"/><path d="M1.2 5 H8.8" stroke="#fff" stroke-width="0.8"/></svg></span>
        Copperbidhouse.net
      </li>
      <li class="contact-item">
        <span class="contact-icon"><svg viewBox="0 0 10 10"><path d="M5 9.3 Q1.8 5.8 1.8 4 A3.2 3.2 0 0 1 8.2 4 Q8.2 5.8 5 9.3Z" fill="#fff"/><circle cx="5" cy="4" r="1.2" fill="#d5282c"/></svg></span>
        418 Birchmont Road Suite
      </li>
      <li class="contact-item continued">200C Fenwick NY 11093</li>
    </ul>
    <div class="divider"></div>
    <div class="brand">
      <span class="brand-mark"></span>
      <span class="brand-name">Copper Gavel<br>Auctions</span>
    </div>
    <div class="social-row" aria-label="Social profiles">
      <span class="social-dot"></span>
      <span class="social-dot"></span>
      <span class="social-dot"></span>
      <span class="social-dot"></span>
    </div>
  </section>
</body>
</html>
```